Front book cover for a training course to help bakers get higher prices and sell more wedding cakes.

We need a front cover for a book that will be teaching bakers how to sell wedding cakes to get higher prices and book more orders. It is a business book. Do not make it look like we want brides to read it. Bakers will be judging the cover to see if it is worth their investment to read it. The title is already in the logo, so do not repeat it.

Target Market(s)

Bakers who sell wedding cakes

Industry/Entity Type

Bakery

Colors

Designer to choose colors to be used in the design.

Requirements
Must have
• Must use the logo. Must have author name: Lou Brand. Must have subtitle: Raise Your Margin. Land More Orders. Scale Your Bakery.
Nice to have
• You are free to be creative. The concept is not to be pretty. It is a business sales and marketing book

```html
<!DOCTYPE html>
<html lang="en">
<head>
<meta charset="utf-8">
<title>Raise Your Margin. Land More Orders. Scale Your Bakery. — Lou Brand</title>
<link rel="stylesheet" href="https://fonts.googleapis.com/css2?family=Russo+One&family=Montserrat:wght@300;500&display=swap">
<style>
  :root {
    --paper: #f2f2f2;
    --paper-edge: #e8e8e8;
    --ink: #55565a;
    --accent: #ee4f7d;
    --on-accent: #ffffff;
  }
  html, body {
    margin: 0;
    padding: 0;
    width: 800px;
    height: 1200px;
    overflow: hidden;
    background: var(--paper);
  }
  .cover {
    position: relative;
    width: 800px;
    height: 1200px;
    background: radial-gradient(ellipse at center, var(--paper) 55%, var(--paper-edge) 100%);
    overflow: hidden;
  }
  .brand {
    position: absolute;
    top: 196px;
    left: 0;
    width: 800px;
    height: 80px;
    display: flex;
    align-items: center;
    justify-content: center;
    gap: 18px;
  }
  .brand__mark {
    width: 36px;
    height: 36px;
    background: var(--accent);
  }
  .brand__name {
    font-family: "Russo One", sans-serif;
    font-size: 62px;
    line-height: 1;
    color: var(--ink);
  }
  .headline {
    margin: 0;
    font-weight: 400;
  }
  .headline-word,
  .subtitle-band {
    position: absolute;
    left: 117px;
    width: 566px;
    display: flex;
    align-items: center;
    justify-content: center;
  }
  .headline-word {
    font-family: "Russo One", sans-serif;
    line-height: 1;
    color: var(--ink);
    letter-spacing: 2px;
    white-space: nowrap;
  }
  .headline-word__text {
    display: inline-block;
    transform-origin: center;
  }
  .headline-word--raise { top: 320px; height: 120px; font-size: 128px; }
  .headline-word--raise .headline-word__text { transform: scaleX(1.24); }
  .headline-word--land  { top: 588px; height: 124px; font-size: 142px; }
  .headline-word--land .headline-word__text { transform: scaleX(1.36); }
  .headline-word--scale { top: 852px; height: 124px; font-size: 142px; }
  .headline-word--scale .headline-word__text { transform: scaleX(1.1); }
  .subtitle-band {
    height: 80px;
    background: var(--accent);
    font-family: "Montserrat", sans-serif;
    font-weight: 500;
    font-size: 54px;
    line-height: 1;
    color: var(--on-accent);
    letter-spacing: 4px;
    white-space: nowrap;
  }
  .subtitle-band--margin { top: 460px; }
  .subtitle-band--orders { top: 722px; }
  .subtitle-band--bakery { top: 988px; }
  .author {
    position: absolute;
    top: 1116px;
    left: 0;
    width: 800px;
    text-align: center;
    font-family: "Montserrat", sans-serif;
    font-weight: 300;
    font-size: 42px;
    letter-spacing: 9px;
    color: var(--ink);
    text-transform: uppercase;
    margin: 0;
  }
</style>
</head>
<body>
  <main class="cover">
    <div class="brand">
      <span class="brand__mark" aria-hidden="true"></span>
      <span class="brand__name">Tier Profit Coach</span>
    </div>

    <h1 class="headline">
      <span class="headline-word headline-word--raise"><span class="headline-word__text">RAISE</span></span>
      <span class="subtitle-band subtitle-band--margin">YOUR MARGIN.</span>
      <span class="headline-word headline-word--land"><span class="headline-word__text">LAND</span></span>
      <span class="subtitle-band subtitle-band--orders">MORE ORDERS.</span>
      <span class="headline-word headline-word--scale"><span class="headline-word__text">SCALE</span></span>
      <span class="subtitle-band subtitle-band--bakery">YOUR BAKERY.</span>
    </h1>

    <p class="author">Lou Brand</p>
  </main>
</body>
</html>
```